GraniteLoop. Customer needs to know about us, what services we provide & contact us

We are a waste tire recycling company. Our primary focus is on providing a sustainable and cost effective service focusing on: Waste Tire Management, Hassle Free Scheduling for Tire Collection, Mobile Shredding & Special site cleanup services. GraniteLoop will be producing TDF, Clean Tire Wire & further materials.
Please look at https://quorvalwheel.example
Please look at https://bandimacorp.example

This is the look and feel of what we want

I have attached a word document with our website info.

Target Market(s)

Tire Install Companies. Such as paltonhaul.example. TDF Purchasers such as kevrofuel.example.

Industry/Entity Type

Waste Tire Recycling

Coding

Coded - Design and coding required

Number of Pages Required

3 page

Font styles to use
Other font styles liked:
• Look at our logo

Requirements
Must have
• We need a 3 page setup for About Us, Services & Contact Us. Contact us should be a form them can fill out and submit to us Images that are related to waste tire recycling. Clean, modern, innovative.
Nice to have
• The color and feel of the website should work with our logo that we did with artmarketly
Should not have
• Anything progressive, political or "woke"

```html
<!DOCTYPE html>
<html lang="en">
<head>
<meta charset="utf-8">
<title>GraniteLoop – Waste Tire Recycling</title>
<link rel="stylesheet" href="https://fonts.googleapis.com/css2?family=Teko:wght@400;500;600&family=Poppins:wght@400;500&display=swap">
<style>
:root{
  --green:#16a04a;
  --green-dark:#118a3e;
  --ink:#1b1e22;
  --text:#444;
  --muted:#888;
  --line:#e2e2e2;
  --footer:#0b0b0b;
  --footer-bar:#1c1c1c;
  --white:#fff;
}
*{box-sizing:border-box;margin:0;padding:0}
html,body{width:1200px;height:4110px;overflow:hidden;background:var(--white)}
body{position:relative;font-family:"Poppins",sans-serif;color:var(--text)}
.abs{position:absolute}
.display{font-family:"Teko",sans-serif;font-weight:500;color:var(--ink);letter-spacing:1px;line-height:1}
.btn{position:absolute;display:flex;align-items:center;justify-content:center;background:var(--green);color:var(--white);font-family:"Teko",sans-serif;font-weight:500;font-size:19px;letter-spacing:1.2px;text-transform:uppercase}
.photo{position:absolute}
.dots{position:absolute;background-image:radial-gradient(#b9bfc4 1.3px,transparent 1.6px);background-size:8px 8px}

/* header */
.brand{left:54px;top:16px;height:36px;display:flex;align-items:center;gap:8px;font-family:"Poppins",sans-serif;font-weight:500;font-size:22px;color:var(--green)}
.brand .mark{width:14px;height:14px;border-radius:50%;background:var(--green)}
.nav{top:24px;left:768px;display:flex;gap:28px;font-size:14px;color:#333}
.nav a{color:inherit;text-decoration:none}

/* hero */
.hero{left:54px;top:67px;width:1092px;height:547px;background:linear-gradient(180deg,#4b5149 0%,#2f342f 50%,#1f231f 100%)}
.hero-line{position:absolute;top:0;width:1px;height:547px;background:rgba(255,255,255,.45)}
.hero-title{position:absolute;top:168px;width:100%;text-align:center;color:var(--white);font-size:64px;font-weight:400}
.hero-sub{position:absolute;top:246px;width:100%;text-align:center;color:#eee;font-size:13.5px;line-height:24px}

/* services */
.service-photo{left:156px;top:726px;width:395px;height:449px;background:linear-gradient(160deg,#8c8f86 0%,#3a3d3a 60%,#232523 100%)}
.service-heading{left:156px;top:985px;width:395px;text-align:center;color:var(--white);font-size:48px;font-weight:400}
.card{position:absolute;width:222px;border:1px solid var(--line);background:var(--white);text-align:center}
.card svg{margin:24px auto 0;display:block}
.card h3{font-family:"Teko",sans-serif;font-weight:500;font-size:19px;letter-spacing:1px;color:var(--ink);margin-top:14px}
.card p{font-size:11.5px;line-height:19px;color:#555;padding:10px 20px 0}

/* section titles */
.sec-title{position:absolute;left:0;width:1200px;text-align:center;font-size:46px;font-weight:400}
.rule{position:absolute;left:571px;width:58px;height:3px;background:var(--green)}
.lead{position:absolute;left:320px;width:560px;text-align:center;font-size:13px;line-height:24px;color:#444}

/* tiles */
.tile{position:absolute;width:254px;height:228px;background:linear-gradient(170deg,#6d716d 0%,#3c3f3c 60%,#2a2c2a 100%)}
.tile .label{position:absolute;left:24px;right:24px;background:rgba(240,240,240,.93);display:flex;flex-direction:column;align-items:center;justify-content:center;text-align:center;font-family:"Teko",sans-serif;font-weight:500;font-size:18px;line-height:23px;letter-spacing:1px;color:#222}
.tile .label::after{content:"";width:60px;height:2px;background:var(--green);margin-top:10px}
.tile.active .label{background:var(--green);color:var(--white);left:24px;right:24px;top:24px;bottom:0}
.tile.active .label::after{display:none}
.tile.active p{font-family:"Poppins",sans-serif;font-size:11.5px;line-height:18px;letter-spacing:0;margin-top:14px}

/* experience */
.years{left:0;width:1200px;top:1978px;text-align:center;font-size:200px;font-weight:500;letter-spacing:14px;color:#1d2126}
.exp{left:0;width:1200px;top:2180px;text-align:center;font-size:46px;font-weight:400}
.exp-line{position:absolute;top:2202px;height:1px;background:#c8c8c8}

/* produce */
.tabs{left:156px;top:2490px;display:flex;gap:0;font-family:"Teko",sans-serif;font-size:19px;font-weight:500;letter-spacing:1px;color:#222}
.tabs span{display:block}
.tabs .on{color:var(--green);border-bottom:2px solid var(--green);padding-bottom:2px}
.produce-text{left:156px;top:2545px;width:400px;font-size:12.5px;line-height:24px;color:#444}

/* testimonials */
.quote{position:absolute;top:2978px;width:280px;height:315px;border:1px solid var(--line);text-align:center}
.avatar{position:absolute;top:-48px;left:92px;width:96px;height:96px;border-radius:50%;border:4px solid #eee;background:linear-gradient(180deg,#c7cbd1,#8c95a1)}
.quote h4{margin-top:72px;font-family:"Teko",sans-serif;font-weight:500;font-size:24px;letter-spacing:1px;color:var(--ink)}
.quote p{padding:8px 22px 0;font-size:11.5px;line-height:19.5px;color:#444}
.stars{margin-top:12px;display:flex;justify-content:center;gap:4px}

/* dealer band */
.band{left:0;top:3374px;width:1200px;height:190px;background:var(--green)}
.band-title{position:absolute;left:156px;top:72px;display:flex;align-items:center;gap:12px;color:var(--white);font-size:48px;font-weight:400}
.btn-ghost{position:absolute;left:892px;top:72px;width:152px;height:46px;background:var(--white);color:var(--green);display:flex;align-items:center;justify-content:center;font-family:"Teko",sans-serif;font-size:17px;font-weight:500;letter-spacing:1.2px}

/* footer */
.footer{left:0;top:3564px;width:1200px;height:499px;background:var(--footer)}
.f-brand{left:156px;top:3656px;display:flex;align-items:center;gap:8px;color:var(--green);font-size:24px;font-weight:500}
.f-brand .mark{width:14px;height:14px;border-radius:50%;background:var(--green)}
.f-about{left:156px;top:3722px;width:320px;color:#ddd;font-size:12.5px;line-height:23px}
.f-key{position:absolute;left:156px;font-family:"Teko",sans-serif;font-size:22px;letter-spacing:1px;color:var(--green)}
.f-val{position:absolute;left:255px;width:250px;color:#ddd;font-size:12.5px;line-height:22px}
.f-head{position:absolute;top:3654px;font-family:"Teko",sans-serif;font-size:30px;letter-spacing:1px;color:var(--green)}
.field{position:absolute;left:538px;width:328px;background:#2a2a2a;color:#ccc;font-size:12px;padding:16px 15px}
.send{position:absolute;left:538px;top:3934px;width:328px;height:49px;background:var(--white);color:var(--green);display:flex;align-items:center;justify-content:center;font-family:"Teko",sans-serif;font-size:18px;font-weight:500;letter-spacing:1.2px}
.f-link{position:absolute;left:916px;font-family:"Teko",sans-serif;font-size:23px;letter-spacing:1px;color:var(--white)}
.copy{left:0;top:4063px;width:1200px;height:47px;background:var(--footer-bar);color:#ddd;font-size:12px;display:flex;align-items:center;justify-content:center}
</style>
</head>
<body>

<header>
  <div class="abs brand"><span class="mark"></span>GraniteLoop</div>
  <nav class="abs nav"><a>About Us</a><a>Service</a><a>Contact Us</a></nav>
  <svg class="abs" style="left:1076px;top:24px" width="20" height="20" viewBox="0 0 20 20" fill="none" stroke="#333" stroke-width="1.8"><circle cx="8" cy="8" r="6"/><path d="M12.5 12.5L18 18"/></svg>
  <svg class="abs" style="left:1118px;top:24px" width="28" height="18" viewBox="0 0 28 18" stroke="#333" stroke-width="2"><path d="M4 2h24M0 9h28M8 16h20"/></svg>
</header>

<section class="abs hero" role="img" aria-label="Yard stacked with mounds of scrap tires and a loader">
  <span class="hero-line" style="left:273px"></span>
  <span class="hero-line" style="left:546px"></span>
  <span class="hero-line" style="left:819px"></span>
  <span class="abs" style="left:545px;top:86px;width:3px;height:30px;background:var(--green)"></span>
  <span class="abs" style="left:272px;top:346px;width:3px;height:30px;background:var(--green)"></span>
  <span class="abs" style="left:818px;top:424px;width:3px;height:30px;background:var(--green)"></span>
  <h1 class="display hero-title">WECOME TO GRANITELOOP</h1>
  <p class="hero-sub">Lorem ipsum dolor sit amet, consectetur adipiscing elit, sed do eiusmod<br>tempor incididunt ut labore et dolore magna aliqua.</p>
</section>
<a class="btn" style="left:487px;top:386px;width:226px;height:45px">Start Recycling With Us</a>

<section>
  <div class="dots" style="left:128px;top:694px;width:276px;height:20px"></div>
  <div class="dots" style="left:128px;top:714px;width:20px;height:260px"></div>
  <div class="photo service-photo" role="img" aria-label="Worker in orange overalls sorting a pile of used tires"></div>
  <h2 class="abs display service-heading">OUR SERVICES</h2>
  <a class="btn" style="left:260px;top:1080px;width:188px;height:46px">See Our Services</a>

  <div class="card" style="left:576px;top:726px;height:211px">
    <svg width="46" height="46" viewBox="0 0 46 46"><circle cx="23" cy="23" r="20" fill="var(--green)"/><circle cx="23" cy="23" r="11" fill="none" stroke="#fff" stroke-width="3"/><circle cx="23" cy="23" r="3" fill="#fff"/></svg>
    <h3>WASTE TIRE MANAGEMENT</h3>
    <p>Lorem ipsum dolor sit amet, consectetur adipiscing elit, sed do eiusmod</p>
  </div>
  <div class="card" style="left:822px;top:726px;height:211px">
    <svg width="46" height="46" viewBox="0 0 46 46"><rect x="4" y="8" width="34" height="32" rx="3" fill="var(--green)"/><rect x="4" y="8" width="34" height="8" fill="#0c6e30"/><circle cx="36" cy="34" r="8" fill="#fff" stroke="#222" stroke-width="2"/><path d="M36 30v4h3" stroke="#222" stroke-width="2" fill="none"/></svg>
    <h3>HASSLE FREE SCHEDULING</h3>
    <p>Lorem ipsum dolor sit amet, consectetur adipiscing elit, sed do eiusmod</p>
  </div>
  <div class="card" style="left:576px;top:962px;height:213px">
    <svg width="46" height="46" viewBox="0 0 46 46"><rect x="9" y="4" width="28" height="20" fill="#fff" stroke="#222" stroke-width="2"/><rect x="6" y="20" width="34" height="22" fill="var(--green)"/><path d="M12 26v14M17 26v14M22 26v14M27 26v14M32 26v14" stroke="#fff" stroke-width="2"/></svg>
    <h3>MOBILE SHREDDING</h3>
    <p>Lorem ipsum dolor sit amet, consectetur adipiscing elit, sed do eiusmod</p>
  </div>
  <div class="card" style="left:822px;top:962px;height:213px">
    <svg width="46" height="46" viewBox="0 0 46 46"><path d="M10 14h26l-3 28H13z" fill="var(--green)"/><rect x="8" y="10" width="30" height="5" fill="#222"/><path d="M18 10V5h10v5" fill="none" stroke="#222" stroke-width="2"/></svg>
    <h3>SPECIAL SITE CLEANUP</h3>
    <p>Lorem ipsum dolor sit amet, consectetur adipiscing elit, sed do eiusmod</p>
  </div>
</section>

<section>
  <h2 class="display sec-title" style="top:1252px">WHO WE ARE</h2>
  <span class="rule" style="top:1308px"></span>
  <p class="lead" style="top:1336px">As a company, we are constantly seeking to develop and implement environmentally acceptable and economically viable end-use markets for scrap tires to increase the recycling and the reuse endeavors for end-of-life regeneration of the scrap tire</p>

  <div class="tile" style="left:54px;top:1449px" role="img" aria-label="Blue recycling bins beside stacked tires"><div class="label" style="top:67px;height:93px">THE BENEFITS OF<br>TIRE RECYCLING</div></div>
  <div class="tile" style="left:334px;top:1449px" role="img" aria-label="Stacks of worn tires"><div class="label" style="top:72px;height:80px">THE FUTURE OF TIRES</div></div>
  <div class="tile active" style="left:613px;top:1449px" role="img" aria-label="Close-up of tire treads">
    <div class="label">
      <svg width="26" height="26" viewBox="0 0 26 26" fill="none" stroke="#fff" stroke-width="1.8"><circle cx="11" cy="11" r="8"/><path d="M17 17l7 7M11 7v8M7 11h8"/></svg>
      <div style="margin-top:8px">IT'S TIME TO<br>RE-PURPOSE</div>
      <p>Lorem ipsum dolor sit amet,<br>consectetur adipiscing elit,</p>
    </div>
  </div>
  <div class="tile" style="left:892px;top:1449px" role="img" aria-label="Large stockpile of tires"><div class="label" style="top:68px;height:93px">DANGERS OF TIRE<br>STOCKPILES</div></div>

  <div class="tile" style="left:54px;top:1705px" role="img" aria-label="Row of discarded tires"><div class="label" style="top:70px;height:90px">CEASE PREVENTABLE<br>DISEASES</div></div>
  <div class="tile" style="left:334px;top:1705px" role="img" aria-label="Mechanic fitting a wheel"><div class="label" style="top:76px;height:78px">FIRE DANGER</div></div>
  <div class="tile" style="left:613px;top:1705px" role="img" aria-label="Recycling bins at a tire yard"><div class="label" style="top:70px;height:90px">TIRE TODAY,<br>TRANSFORMED TOMORROW</div></div>
  <div class="tile" style="left:892px;top:1705px" role="img" aria-label="Tires piled at a landfill"><div class="label" style="top:68px;height:90px">GOODBYE OVERFLOWING<br>LANDFILLS</div></div>
</section>

<section>
  <div class="abs display years">20 YEARS</div>
  <span class="exp-line" style="left:155px;width:305px"></span>
  <span class="exp-line" style="left:742px;width:302px"></span>
  <h2 class="abs display exp">OF EXPERIENCE</h2>
  <a class="btn" style="left:506px;top:2266px;width:188px;height:47px">Make an Appoinment</a>
</section>

<section>
  <h2 class="abs display" style="left:156px;top:2414px;font-size:46px;font-weight:400">WHAT WE PRODUCE</h2>
  <div class="abs tabs">
    <span class="on">TDF</span>
    <span style="margin-left:74px">CLEAN TIRE WIRE</span>
    <span style="margin-left:72px">FURTHER MATERIALS</span>
  </div>
  <p class="abs produce-text">Tire Derived Fuel (TDF) is produced at our plant to supply a steady, low-cost energy source as a part of our 'Cleaner Roads' initiative. It is a programme of GraniteLoop (Waste Tire Division) managed by our plant team meeting the needs of cement kilns, paper mills and utility boilers.</p>
  <a class="btn" style="left:156px;top:2696px;width:152px;height:46px">View Details</a>
  <div class="dots" style="left:622px;top:2393px;width:270px;height:16px"></div>
  <div class="dots" style="left:622px;top:2409px;width:20px;height:310px"></div>
  <div class="photo" style="left:648px;top:2418px;width:396px;height:324px;background:linear-gradient(170deg,#b5b8b6 0%,#6d706f 35%,#2f3232 100%)" role="img" aria-label="Conveyor dropping shredded tire crumb onto a pile"></div>
</section>

<section>
  <h2 class="display sec-title" style="top:2818px">WHAT PEOPLE SAYS</h2>
  <span class="rule" style="top:2878px"></span>
  <div class="quote" style="left:156px"><div class="avatar" role="img" aria-label="Customer portrait"></div><h4>DANIEL MERCER</h4><p>Nora, Owen and the Harbor Line Creative team are amazing! They are always available and truly work diligently to obtain the best possible ROI. Thank you for all you do and continue to do for my law firm. I look forward to amazing future growth with you as my team.</p><div class="stars"><svg width="92" height="16" viewBox="0 0 92 16" fill="#f4b400"><path id="st" d="M8 0l2.4 5 5.4.6-4 3.7 1.1 5.4L8 12l-4.9 2.7 1.1-5.4-4-3.7 5.4-.6z"/><use href="#st" x="19"/><use href="#st" x="38"/><use href="#st" x="57"/><use href="#st" x="76"/></svg></div></div>
  <div class="quote" style="left:460px"><div class="avatar" role="img" aria-label="Customer portrait"></div><h4>DANIEL MERCER</h4><p>Nora, Owen and the Harbor Line Creative team are amazing! They are always available and truly work diligently to obtain the best possible ROI. Thank you for all you do and continue to do for my law firm. I look forward to amazing future growth with you as my team.</p><div class="stars"><svg width="92" height="16" viewBox="0 0 92 16" fill="#f4b400"><use href="#st"/><use href="#st" x="19"/><use href="#st" x="38"/><use href="#st" x="57"/><use href="#st" x="76"/></svg></div></div>
  <div class="quote" style="left:764px"><div class="avatar" role="img" aria-label="Customer portrait"></div><h4>DANIEL MERCER</h4><p>Nora, Owen and the Harbor Line Creative team are amazing! They are always available and truly work diligently to obtain the best possible ROI. Thank you for all you do and continue to do for my law firm. I look forward to amazing future growth with you as my team.</p><div class="stars"><svg width="92" height="16" viewBox="0 0 92 16" fill="#f4b400"><use href="#st"/><use href="#st" x="19"/><use href="#st" x="38"/><use href="#st" x="57"/><use href="#st" x="76"/></svg></div></div>
</section>

<section class="abs band">
  <h2 class="display band-title"><svg width="24" height="32" viewBox="0 0 24 32"><path d="M12 0C5.4 0 0 5.3 0 11.8 0 20.6 12 32 12 32s12-11.4 12-20.2C24 5.3 18.6 0 12 0z" fill="#fff"/><circle cx="12" cy="11.5" r="4.5" fill="var(--green)"/></svg><span style="color:#fff;padding-top:6px">FIND A DEALER NEAR YOU</span></h2>
  <a class="btn-ghost">CONATCT US</a>
</section>

<footer>
  <div class="abs footer"></div>
  <div class="abs f-brand"><span class="mark"></span>GraniteLoop</div>
  <p class="abs f-about">We are an industry-leading and award-winning construction services provider ready to work on a project of any complexity, whether it's commercial or residential.</p>
  <span class="f-key" style="top:3850px">LOCATION</span>
  <span class="f-val" style="top:3850px">1850 Cedar Basin Rd, Fallow Creek, CA 90413</span>
  <span class="f-key" style="top:3918px">PHONE</span>
  <span class="f-val" style="top:3918px">+1 555-014-2290, +1 555-017-3381</span>
  <span class="f-key" style="top:3965px">E-MAIL</span>
  <span class="f-val" style="top:3965px">info@graniteloop.example</span>

  <h3 class="f-head" style="left:538px">FIND A DEALER NEAR YOU</h3>
  <div class="field" style="top:3714px;height:48px">Name</div>
  <div class="field" style="top:3773px;height:48px">E-mails</div>
  <div class="field" style="top:3832px;height:91px">Message</div>
  <a class="send">SEND MESSAGE</a>

  <h3 class="f-head" style="left:916px">QUICK LINKS</h3>
  <a class="f-link" style="top:3710px">ABOUT US</a>
  <a class="f-link" style="top:3767px">SERVICE</a>
  <a class="f-link" style="top:3825px">CONTACT US</a>

  <div class="abs copy">© 2022 GraniteLoop | All rights reserved | Privacy Policy</div>
</footer>

</body>
</html>
```